Ashcombe Ridge Business Cards

We need business card designs for a modern home development, Ashcombe Ridge. We would like to see modern looking designs- clean and simple but striking. I've attached some images of one of the homes so you can see the style of the homes we are putting on the market and perhaps they will inspire your design! I've also attached the logo- both horizontal and vertical. We need to use the logo on the card. I've also attached a sign that has a map of the development. If you can use that and still keep the card nice and clean, great. If not, it's not a problem to leave the map out completely.

```html
<!DOCTYPE html>
<html lang="en">
<head>
<meta charset="utf-8">
<title>Ashcombe Ridge Business Card</title>
<link rel="stylesheet" href="https://fonts.googleapis.com/css2?family=Didact+Gothic&display=swap">
<style>
  :root {
    --page-bg: #e4e4e2;
    --card-bg: #f4f4f3;
    --ink-dark: #3b3f43;
    --ink-mid: #6a6e72;
    --accent-teal: #1d7f8f;
    --card-shadow: rgba(0, 0, 0, 0.18);
  }
  * { margin: 0; padding: 0; box-sizing: border-box; }
  html, body {
    width: 1200px;
    height: 900px;
    overflow: hidden;
    background: var(--page-bg);
  }
  .canvas {
    width: 1200px;
    height: 900px;
    display: flex;
    flex-direction: column;
    align-items: center;
    justify-content: center;
    gap: 36px;
  }
  .business-card {
    position: relative;
    width: 680px;
    height: 389px;
    background: var(--card-bg);
    box-shadow: 0 10px 30px var(--card-shadow);
    font-family: "Didact Gothic", sans-serif;
  }
  .brand-lockup {
    display: flex;
    align-items: center;
    gap: 11px;
  }
  .brand-square {
    width: 27px;
    height: 27px;
    background: var(--accent-teal);
  }
  .brand-name {
    font-size: 23px;
    letter-spacing: 0.7px;
    color: var(--ink-dark);
    line-height: 1;
    white-space: nowrap;
  }
  .card-back {
    display: flex;
    align-items: center;
    justify-content: center;
  }
  .card-front .brand-lockup {
    position: absolute;
    left: 57px;
    top: 150px;
  }
  .contact-block {
    position: absolute;
    left: 340px;
    top: 130px;
    color: var(--ink-mid);
    letter-spacing: 1.6px;
    white-space: nowrap;
  }
  .person-name {
    font-size: 17px;
    color: var(--ink-dark);
    font-weight: 400;
    -webkit-text-stroke: 0.4px var(--ink-dark);
  }
  .person-title {
    margin-top: 5px;
    font-size: 13px;
    color: var(--accent-teal);
  }
  .address {
    margin-top: 26px;
    font-size: 13px;
    line-height: 1.6;
    font-style: normal;
  }
  .contact-list {
    list-style: none;
    margin-top: 3px;
    font-size: 13px;
    line-height: 1.6;
  }
  .contact-item {
    position: relative;
  }
  .contact-icon {
    position: absolute;
    left: -22px;
    top: 4px;
    width: 14px;
    height: 13px;
  }
</style>
</head>
<body>
  <main class="canvas">
    <article class="business-card card-back">
      <div class="brand-lockup">
        <span class="brand-square"></span>
        <span class="brand-name">Ashcombe Ridge</span>
      </div>
    </article>

    <article class="business-card card-front">
      <div class="brand-lockup">
        <span class="brand-square"></span>
        <span class="brand-name">Ashcombe Ridge</span>
      </div>

      <section class="contact-block">
        <h1 class="person-name">Carolyn J. Whitfield</h1>
        <p class="person-title">Jr. Developer, Construction Manager</p>
        <address class="address">
          2470 Larkspur Avenue<br>
          Dallas, TX 75206
        </address>
        <ul class="contact-list">
          <li class="contact-item">
            <svg class="contact-icon" viewBox="0 0 20 18" aria-hidden="true">
              <path d="M2 6 Q10 0 18 6 L16 8 L13 6 L13 4 Q10 3 7 4 L7 6 L4 8 Z" fill="var(--accent-teal)"/>
              <rect x="4" y="9" width="12" height="7" rx="1.5" fill="var(--accent-teal)"/>
            </svg>
            214.555.0148
          </li>
          <li class="contact-item">
            <svg class="contact-icon" viewBox="0 0 20 18" aria-hidden="true">
              <rect x="1.5" y="2.5" width="17" height="13" fill="none" stroke="var(--accent-teal)" stroke-width="2"/>
              <path d="M1.5 2.5 L10 10 L18.5 2.5" fill="none" stroke="var(--accent-teal)" stroke-width="2"/>
            </svg>
            ashcomberidge@mailbox.net
          </li>
        </ul>
      </section>
    </article>
  </main>
</body>
</html>
```